Leadvista.com ;Take Yourself Up to the Next Level. More success, higher productivity, better health.

PLEASE READ IT CAREFULLY
I HAVE RECEIVED SOME FIRST DESIGNS AND I HAVE A FEELING THAT ALMOST NOBODY HAS READ THE BRIEFING CAREFULLY.

What I need actually is the design of the main visual
THE MAIN VISUAL MUST COMMUNICATE THE CONCEPT.
THIS WEBSITE IS ABOUT THE PERSONAL DEVELOPMENT.

The change of the main visual may be linked with other changes of other elements of the homepage, but this is the secondary task.

BACKGROUND
I have launched a blog on healthy productivity: leadvista.com

The problem is that the main visual does not communicate clearly what the website is about.

Currently I have a blog with advice on healthy productivity and a shop. In teh future I would like to offer stress management courses, fitness boot camps for executives, mindefulness courses, courses for healthy sleep and work-life balance.

The task is to develop the homepage which communicates the current positioning:

Lead Vista-
Take Yourself Up to the Next Level. More Success, Higher Productivity, Better Health.

The homepage should contain all the blocks of the current homepage. Actually the main task is to find the powerful design representation of the website positioning.
Updates

Low design quality

Target Market(s)

US executives, managers and entrepreneurs

Requirements
Must have
• You should keep in principle the current color code which is green, blue, grey
• The design project must contain all the current homepage elements like blog, testimonial, footnote etc

```html
<!DOCTYPE html>
<html lang="en">
<head>
<meta charset="utf-8">
<title>Leadvista – Healthy Productivity</title>
<link href="https://fonts.googleapis.com/css2?family=Merriweather:wght@700;900&family=Roboto:wght@400;500;700&display=swap" rel="stylesheet">
<style>
  :root {
    --green: #82b843;
    --green-line: #d8ecc2;
    --blue: #6e8fb3;
    --grey-dark: #555a5e;
    --grey-line: #9aa0a4;
    --page: #f6f7f9;
    --white: #ffffff;
  }
  * { box-sizing: border-box; margin: 0; padding: 0; }
  html, body { width: 1200px; height: 1200px; overflow: hidden; background: var(--white); }
  body { font-family: "Roboto", sans-serif; position: relative; }
  .site { position: absolute; left: 46px; top: 0; width: 1104px; height: 1200px; background: var(--page); }
  .header { height: 58px; background: var(--white); position: relative; }
  .brand { position: absolute; left: 30px; top: 16px; font-size: 24px; font-weight: 500; color: var(--grey-dark); letter-spacing: 2px; }
  .social { position: absolute; right: 26px; top: 20px; display: flex; gap: 14px; }
  .social span { width: 22px; height: 22px; border-radius: 50%; background: var(--grey-dark); display: block; }
  .nav { height: 47px; background: var(--green); display: flex; position: relative; padding-left: 28px; }
  .nav a { color: var(--white); text-decoration: none; font-size: 14px; display: flex; align-items: center; padding: 0 25px; border-right: 1px solid rgba(255,255,255,0.25); }
  .nav a.active { background: var(--blue); padding: 0 28px; }
  .nav a:last-of-type { border-right: none; }
  .nav .search { position: absolute; right: 38px; top: 13px; }
  .hero { position: relative; height: 584px; background: linear-gradient(180deg, #8a9a78 0%, #6d7a62 35%, #5e6558 60%, #6a7659 100%); overflow: hidden; }
  .hero-photo { position: absolute; inset: 0; background: radial-gradient(ellipse at 50% 45%, rgba(150,150,150,0.55), rgba(60,70,55,0.2) 70%), linear-gradient(90deg, rgba(80,95,70,0.6), rgba(120,125,120,0.2) 50%, rgba(70,90,50,0.6)); }
  .hero-title { position: absolute; top: 140px; width: 100%; text-align: center; font-family: "Merriweather", serif; font-weight: 900; font-size: 42px; color: var(--white); }
  .hero-sub { position: absolute; top: 208px; width: 100%; text-align: center; font-size: 26px; color: var(--white); }
  .hero-cta { position: absolute; top: 328px; left: 402px; width: 292px; height: 61px; background: var(--blue); color: var(--white); font-weight: 700; font-size: 20px; display: flex; align-items: center; justify-content: center; letter-spacing: 0.3px; }
  .arrow { position: absolute; top: 237px; width: 33px; height: 56px; background: rgba(110,143,179,0.85); display: flex; align-items: center; justify-content: center; }
  .arrow.prev { left: 14px; } .arrow.next { right: 14px; }
  .about { position: absolute; left: 104px; top: 582px; width: 896px; height: 314px; background: var(--green); box-shadow: 0 2px 4px rgba(0,0,0,0.25); text-align: center; color: var(--white); }
  .about h2 { font-family: "Merriweather", serif; font-weight: 700; font-size: 26px; margin-top: 20px; }
  .divider { position: relative; height: 30px; margin-top: 6px; }
  .divider::before, .divider::after { content: ""; position: absolute; top: 14px; height: 1px; }
  .divider i { position: absolute; left: 50%; top: 7px; width: 14px; height: 14px; margin-left: -7px; border-radius: 50%; }
  .about .divider { margin: 6px 18px 0; }
  .about .divider::before { left: 0; right: calc(50% + 26px); background: var(--green-line); }
  .about .divider::after { right: 0; left: calc(50% + 26px); background: var(--green-line); }
  .about .divider i { background: var(--grey-dark); }
  .about p { font-size: 20.5px; line-height: 25.5px; padding: 0 40px; margin-top: 12px; }
  .about p + p { margin-top: 25px; }
  .shop { position: absolute; top: 936px; left: 0; width: 100%; text-align: center; }
  .shop h2 { font-family: "Merriweather", serif; font-weight: 700; font-size: 26px; color: var(--green); }
  .shop .divider { margin: 8px 14px 0; }
  .shop .divider::before { left: 0; right: calc(50% + 26px); background: var(--grey-line); }
  .shop .divider::after { right: 0; left: calc(50% + 26px); background: var(--grey-line); }
  .shop .divider i { background: var(--grey-dark); }
  .categories { position: absolute; top: 104px; left: 0; width: 100%; }
  .category { position: absolute; width: 160px; margin-left: -80px; text-align: center; }
  .category svg { display: block; margin: 0 auto; }
  .category span { display: block; margin-top: 26px; color: var(--green); font-weight: 500; font-size: 16px; }
</style>
</head>
<body>
<div class="site">
  <header class="header">
    <div class="brand">Leadvista</div>
    <div class="social"><span></span><span></span><span></span><span></span><span></span></div>
  </header>
  <nav class="nav">
    <a class="active">HOME</a><a>ABOUT</a><a>SHOP</a><a>BOOKS</a><a>BLOG</a><a>EXECUTIVE HEALTH</a><a>CONTACT US</a>
    <svg class="search" width="20" height="20" viewBox="0 0 20 20"><circle cx="8" cy="8" r="6" fill="none" stroke="#fff" stroke-width="2"/><line x1="12.5" y1="12.5" x2="18" y2="18" stroke="#fff" stroke-width="2.5"/></svg>
  </nav>
  <section class="hero">
    <div class="hero-photo" role="img" aria-label="Photo of four business people walking through a green park"></div>
    <h1 class="hero-title">BE HEALTHY! BE SUCCESSFUL!</h1>
    <p class="hero-sub">Your guides to healthy productivity.</p>
    <div class="hero-cta">SUBSCRIBE NOW</div>
    <div class="arrow prev"><svg width="14" height="26" viewBox="0 0 14 26"><polyline points="12,2 2,13 12,24" fill="none" stroke="#fff" stroke-width="2"/></svg></div>
    <div class="arrow next"><svg width="14" height="26" viewBox="0 0 14 26"><polyline points="2,2 12,13 2,24" fill="none" stroke="#fff" stroke-width="2"/></svg></div>
  </section>
  <section class="about">
    <h2>ABOUT LEADVISTA</h2>
    <div class="divider"><i></i></div>
    <p>Just by making small changes to your daily routine you can significantly increase your productivity, health and business successJust by making small changes to your daily routine you can significantly increase your productivity, health and business success</p>
    <p>Just by making small changes to your daily routine you can significantly increase your productivity, health and business success</p>
  </section>
  <section class="shop">
    <h2>OUR SHOP</h2>
    <div class="divider"><i></i></div>
    <div class="categories">
      <div class="category" style="left:104px">
        <svg width="88" height="98" viewBox="0 0 88 98"><polygon points="44,2 86,25 86,73 44,96 2,73 2,25" fill="#6e8fb3" stroke="#82b843" stroke-width="3"/><path d="M44 62 L30 48 A8 8 0 0 1 44 38 A8 8 0 0 1 58 48 Z" fill="none" stroke="#fff" stroke-width="2.5"/></svg>
        <span>Health &amp; Productivity</span>
      </div>
      <div class="category" style="left:280px">
        <svg width="88" height="98" viewBox="0 0 88 98"><polygon points="44,2 86,25 86,73 44,96 2,73 2,25" fill="#6e8fb3" stroke="#82b843" stroke-width="3"/><circle cx="40" cy="34" r="6" fill="#fff"/><rect x="44" y="52" width="22" height="4" fill="#fff"/><path d="M28 64 L38 44 L46 54" fill="none" stroke="#fff" stroke-width="5"/></svg>
        <span>Stand &amp; Work</span>
      </div>
      <div class="category" style="left:455px">
        <svg width="88" height="98" viewBox="0 0 88 98"><polygon points="44,2 86,25 86,73 44,96 2,73 2,25" fill="#6e8fb3" stroke="#82b843" stroke-width="3"/><circle cx="44" cy="34" r="8" fill="#fff"/><path d="M28 64 Q28 46 44 46 Q60 46 60 64 Z" fill="#fff"/></svg>
        <span>Active Sitting</span>
      </div>
      <div class="category" style="left:633px">
        <svg width="88" height="98" viewBox="0 0 88 98"><polygon points="44,2 86,25 86,73 44,96 2,73 2,25" fill="#6e8fb3" stroke="#82b843" stroke-width="3"/><circle cx="46" cy="30" r="5" fill="#fff"/><path d="M30 46 L42 40 L50 52 L60 56 M42 40 L36 58" fill="none" stroke="#fff" stroke-width="4"/><line x1="24" y1="66" x2="62" y2="62" stroke="#fff" stroke-width="3"/></svg>
        <span>Exercise</span>
      </div>
      <div class="category" style="left:820px">
        <svg width="88" height="98" viewBox="0 0 88 98"><polygon points="44,2 86,25 86,73 44,96 2,73 2,25" fill="#6e8fb3" stroke="#82b843" stroke-width="3"/><circle cx="44" cy="30" r="5" fill="#fff"/><path d="M38 38 H50 V58 H38 Z" fill="#fff"/><ellipse cx="44" cy="62" rx="16" ry="4" fill="#fff"/></svg>
        <span>Stress &amp; Mediation</span>
      </div>
      <div class="category" style="left:1001px">
        <svg width="88" height="98" viewBox="0 0 88 98"><polygon points="44,2 86,25 86,73 44,96 2,73 2,25" fill="#6e8fb3" stroke="#82b843" stroke-width="3"/><line x1="30" y1="64" x2="58" y2="34" stroke="#fff" stroke-width="5"/><rect x="22" y="54" width="10" height="18" fill="#fff" transform="rotate(45 27 63)"/><rect x="56" y="26" width="10" height="18" fill="#fff" transform="rotate(45 61 35)"/></svg>
        <span>Traveling</span>
      </div>
    </div>
  </section>
</div>
</body>
</html>
```